Semaglutide Diet

A flyer design for a weight loss program based on the peptide Semaglutide that our clinic is rolling out. Here are some very rough ideas

```html
<!DOCTYPE html>
<html lang="en">
<head>
<meta charset="utf-8">
<title>Semaglutide Weight Loss Flyer</title>
<link href="https://fonts.googleapis.com/css2?family=Anton&family=Oswald:wght@300;400&family=Roboto:wght@700&display=swap" rel="stylesheet">
<style>
  :root{
    --red:#e30613;
    --red-deep:#c8141b;
    --blue:#36479a;
    --ink:#1d1d1b;
    --white:#ffffff;
    --grey:#b5b5b5;
    --text:#2a2a2a;
    --backdrop:#ece8e3;
  }
  *{margin:0;padding:0;box-sizing:border-box}
  html,body{width:1200px;height:1200px;overflow:hidden;background:var(--backdrop)}
  .flyer{
    position:absolute;left:160px;top:30px;width:927px;height:1199px;
    transform:scale(.95);transform-origin:0 0;background:var(--white);overflow:hidden;
    box-shadow:0 6px 24px rgba(0,0,0,.25);
  }
  .hero-photo{
    position:absolute;left:0;top:0;width:927px;height:660px;
    background:
      linear-gradient(90deg,var(--red-deep) 0%,rgba(200,20,27,.85) 28%,rgba(120,40,40,.4) 48%,rgba(0,0,0,0) 62%),
      radial-gradient(ellipse at 68% 45%,#6b6258 0%,#2c2a28 45%,#141414 100%);
  }
  .brand{
    position:absolute;left:44px;top:36px;
    font-family:Anton,sans-serif;font-size:60px;line-height:76px;color:var(--white);
  }
  .headline{
    position:absolute;left:44px;top:206px;
    font-family:Anton,sans-serif;font-size:66px;line-height:88px;letter-spacing:-1.5px;
    color:var(--white);text-shadow:3px 3px 0 #1a1a1a;
    transform:scaleX(.93);transform-origin:0 0;
  }
  .swoosh{position:absolute;left:0;top:540px;width:927px;height:120px}
  .product-tab{
    position:absolute;left:0;top:638px;width:532px;height:174px;
    background:var(--ink);border-radius:0 87px 87px 0;
  }
  .product-name{
    position:absolute;left:68px;top:10px;
    font-family:Anton,sans-serif;font-size:96px;line-height:120px;color:var(--white);
    letter-spacing:-1px;transform:scaleX(.88);transform-origin:0 0;
  }
  .product-note{
    position:absolute;left:72px;top:126px;white-space:nowrap;
    font-family:Roboto,Arial,sans-serif;font-weight:700;font-size:23px;color:var(--white);
  }
  .offer{position:absolute;left:650px;top:555px;width:270px;height:260px}
  .offer-text{
    position:absolute;left:700px;top:632px;width:150px;text-align:right;
    font-family:Roboto,Arial,sans-serif;font-weight:700;color:var(--white);
  }
  .offer-text .pct{display:block;font-size:66px;line-height:66px}
  .offer-text .off{display:block;font-size:24px;line-height:22px;margin-right:4px}
  .benefits{
    position:absolute;top:846px;list-style:none;white-space:nowrap;
    font-family:Oswald,sans-serif;font-weight:300;font-size:25px;line-height:30px;color:var(--text);
  }
  .benefits li{position:relative;padding-left:17px;margin-bottom:8px}
  .benefits li::before{content:"•";position:absolute;left:0;top:0}
  .benefits.left{left:77px}
  .benefits.right{left:481px}
  .contact-bar{position:absolute;left:0;top:1122px;width:927px;height:77px}
  .contact-bar svg{position:absolute;inset:0}
  .phone,.email{
    position:absolute;font-family:Roboto,Arial,sans-serif;font-weight:700;color:var(--white);white-space:nowrap;
  }
  .phone{left:37px;top:13px;font-size:37px}
  .email{left:451px;top:19px;font-size:31px}
</style>
</head>
<body>
<main class="flyer">
  <div class="hero-photo" role="img" aria-label="Photo of an athlete training with battle ropes in a gym"></div>

  <div class="brand">YOUR LOGO<br>HERE</div>

  <h1 class="headline">A New,<br>Very Effective<br>Weight loss<br>Pepitde</h1>

  <svg class="swoosh" viewBox="0 0 927 120" preserveAspectRatio="none" aria-hidden="true">
    <path d="M0 30 Q300 -10 700 30 L927 60 L927 120 L0 120Z" fill="var(--blue)"/>
    <path d="M20 100 Q350 20 700 35 Q850 45 927 88 L927 120 L0 120Z" fill="var(--grey)"/>
    <path d="M20 100 Q350 25 690 40 Q830 50 927 95 L927 120 L0 120Z" fill="var(--red)"/>
    <path d="M40 110 Q380 35 690 48 Q830 56 927 100 L927 120 L0 120Z" fill="var(--white)"/>
  </svg>

  <div class="product-tab">
    <div class="product-name">SEMAGLUTIDE</div>
    <div class="product-note">(FDA APPROVED VELORA/GLUMARA)</div>
  </div>

  <svg class="offer" viewBox="0 0 270 260" aria-hidden="true">
    <circle cx="124" cy="123" r="102" fill="var(--red)"/>
    <circle cx="190" cy="52" r="38" fill="var(--red)"/>
    <circle cx="56" cy="12" r="16" fill="var(--red)"/>
    <circle cx="154" cy="2" r="6" fill="var(--red)"/>
    <circle cx="248" cy="63" r="15" fill="var(--red)"/>
    <circle cx="244" cy="100" r="6" fill="var(--red)"/>
    <circle cx="254" cy="172" r="6" fill="var(--red)"/>
    <circle cx="12" cy="156" r="6" fill="var(--red)"/>
    <circle cx="157" cy="232" r="11" fill="var(--red)"/>
  </svg>
  <div class="offer-text"><span class="pct">50%</span><span class="off">Off</span></div>

  <ul class="benefits left">
    <li>ONLINE TELEHEALTH WEIGHT LOSS<br>PROGRAM</li>
    <li>REAL WEIGHT LOSS RESULTS OF UP TO<br>2-4 POUNDS PER WEEK</li>
    <li>REDUCES APPETITE, IMPROVES<br>CONTROL OF EATING AND REDUCES<br>FOOD CRAVINGS</li>
  </ul>
  <ul class="benefits right">
    <li>IMPROVES INSULIN RESISTANCE,<br>BURNS FAT AND BOOSTS ENERGY</li>
    <li>SAFE AND EFFECTIVE ONCE WEEKLY<br>INJECTION</li>
    <li>CAN BE USED IN COMBINATION WITH<br>THE NORVALE HCG PROGRAM OR IN<br>MAINTENANCE PHASE</li>
  </ul>

  <footer class="contact-bar">
    <svg viewBox="0 0 927 77" preserveAspectRatio="none" aria-hidden="true">
      <rect width="927" height="77" fill="var(--red)"/>
      <path d="M0 0 L396 0 L450 77 L0 77Z" fill="var(--blue)"/>
    </svg>
    <div class="phone">Ph.No. : 0123 456789</div>
    <div class="email">Email : yourname@website.com</div>
  </footer>
</main>
</body>
</html>
```